Zielgruppe
Birkenhof Momente in Brandenburg. Husky Wanderungen und Gespannfahrten. Shop Online und vor Ort mit Equipment für Hunde sowie Futter und Beratung.
Aufgabenstellung
Logo mit einbeziehen. Design Richtung Orange gehalten wie Flyer, Logo, Webseite.
Unter folgendem Drive Link noch Bilder von uns sowie Flyer vom Futterladen und Birkenhof Events.
https://files.quellbox-ablage.de/ordner/7tRk2mWq9LxZ4bNvE8cHs3YpUa6Df1Gj?ref=teilen
Beschriftung ist für einen großen weissen Transporter ( Valmora Strada)

```html
<!DOCTYPE html>
<html lang="de">
<head>
<meta charset="utf-8">
<title>Birkenhof Momente – Fahrzeugbeschriftung</title>
<link rel="stylesheet" href="https://fonts.googleapis.com/css2?family=Roboto+Condensed:wght@700;800&family=Poppins:wght@500;600;700&display=swap">
<style>
  :root {
    --orange: #e8870f;
    --ink: #1c1c1c;
    --panel: #ebebeb;
    --panel-light: #f6f6f6;
    --photo-dark: #8e9296;
    --photo-light: #dcdde0;
    --skirt: #1e1e1e;
    --page: #ffffff;
  }
  * { margin: 0; padding: 0; box-sizing: border-box; }
  html, body { width: 1200px; height: 480px; overflow: hidden; background: var(--page); }
  .canvas { position: relative; width: 1200px; height: 480px; font-family: "Poppins", sans-serif; color: var(--ink); }

  .wrap-side {
    position: absolute; left: 160px; top: 45px; width: 880px; height: 370px;
    background: linear-gradient(180deg, var(--panel-light), var(--panel) 70%);
    border-radius: 14px 60px 22px 14px;
    overflow: hidden;
  }
  .skirt { position: absolute; left: 0; right: 0; bottom: 0; height: 40px; background: var(--skirt); }

  .photo-area {
    position: absolute; left: 30px; top: 12px; width: 300px; height: 290px;
    background: radial-gradient(ellipse at 45% 45%, var(--photo-dark), var(--photo-light) 75%, transparent);
  }

  .headline { position: absolute; font-family: "Roboto Condensed", sans-serif; font-weight: 800; color: var(--orange); line-height: 1; font-size: 36px; white-space: nowrap; }
  .headline--top { left: 185px; top: 12px; }
  .headline--bottom { left: 235px; top: 42px; }

  .offer__web { position: absolute; left: 306px; top: 80px; font-size: 17px; line-height: 22px; font-weight: 500; white-space: nowrap; }
  .offer__list { position: absolute; left: 305px; top: 107px; list-style: none; font-size: 13px; font-weight: 500; line-height: 16.3px; white-space: nowrap; }
  .offer__list li::before { content: "• "; }

  .cta__lead { position: absolute; left: 305px; top: 195px; font-size: 13px; line-height: 16px; font-weight: 700; color: var(--orange); white-space: nowrap; }
  .cta__phone { position: absolute; left: 300px; top: 211px; display: flex; align-items: center; gap: 6px; font-size: 17px; line-height: 18px; font-weight: 700; color: var(--orange); white-space: nowrap; }
  .cta__phone svg { width: 15px; height: 15px; }

  .shop-badge {
    position: absolute; left: 28px; top: 200px; width: 158px; height: 52px;
    background: var(--orange); transform: rotate(-9deg);
    display: flex; align-items: center; gap: 7px; padding: 0 8px;
  }
  .shop-badge__dot { width: 22px; height: 22px; border-radius: 50%; background: var(--ink); flex: none; }
  .shop-badge__text { font-size: 6.6px; font-weight: 600; line-height: 1.3; color: var(--ink); white-space: nowrap; }

  .brand { position: absolute; left: 240px; top: 259px; display: flex; align-items: center; gap: 8px; white-space: nowrap; }
  .brand__mark { width: 24px; height: 24px; border-radius: 50%; background: var(--ink); flex: none; }
  .brand__name { font-size: 24px; line-height: 32px; font-weight: 700; color: var(--orange); }

  .hashtag {
    position: absolute; left: 578px; top: 210px; padding: 1px 10px;
    background: var(--orange); font-size: 13px; line-height: 18px; font-weight: 700; color: var(--ink); white-space: nowrap;
  }

  .address { position: absolute; left: 555px; top: 256px; font-size: 7.8px; font-weight: 500; color: var(--orange); line-height: 1.15; white-space: nowrap; }
</style>
</head>
<body>
<main class="canvas">
  <section class="wrap-side">
    <div class="photo-area" role="img" aria-label="Foto zweier laufender Huskys im Schnee"></div>

    <div class="headline headline--top">BIRKENHOF</div>
    <div class="headline headline--bottom">MOMENTE</div>

    <p class="offer__web">auf birkenhof-momente.de</p>
    <ul class="offer__list">
      <li>Wanderungen</li>
      <li>Gespannfahrten</li>
      <li>Firmenevents</li>
      <li>Teambuilding</li>
      <li>und noch Viel mehr!</li>
    </ul>

    <p class="cta__lead">Jetzt Abenteuer planen</p>
    <p class="cta__phone">
      <svg viewBox="0 0 24 24" aria-hidden="true"><path fill="#1c1c1c" d="M6.6 10.8a15.1 15.1 0 0 0 6.6 6.6l2.2-2.2c.3-.3.7-.4 1-.2 1.1.4 2.3.6 3.6.6.6 0 1 .4 1 1V20c0 .6-.4 1-1 1A17 17 0 0 1 3 4c0-.6.4-1 1-1h3.5c.6 0 1 .4 1 1 0 1.3.2 2.5.6 3.6.1.3 0 .7-.2 1z"/></svg>
      0176 42 19 305
    </p>

    <div class="shop-badge">
      <span class="shop-badge__dot"></span>
      <p class="shop-badge__text">Große Auswahl &amp; Qualität<br>an Hundezubehör in<br>unserem Onlineshop auf<br>birkenhof-momente.de</p>
    </div>

    <div class="brand">
      <span class="brand__mark"></span>
      <span class="brand__name">Birkenhof Momente</span>
    </div>

    <div class="hashtag">#birkenhofmomente</div>

    <p class="address">Lindenweg 14<br>16775 Gransee<br>info@birkenhof-momente.de</p>

    <div class="skirt"></div>
  </section>
</main>
</body>
</html>
```